Home Automation Company needs DL size flyer design

We need a flyer that looks like a home control touch panel page on a smartphone. Similar to a "Homevia9" home page. The company is Based in Sydney and named "Allwovenin". We integrate home systems into one central control. Lights, Power, Audio/Visual, Cameras, Security, Access Control, Media Storage. We are inviting people to have their future home now. Looking at new company Logo similar to "Threaded Journal"

Target Market(s)

Home Owners Eastern Suburbs Sydney

Industry/Entity Type

Home Improvement

Contact Information for Business Card

Possibly mini Smartphone look like flyer.

Font styles to use
Other font styles liked:
• TP Black Extended

Colors
cadf82
ffffff
86cfc6
f59195

Requirements
Must have
• A few Media Streaming Services Logos
• Promote ease of use and lifestyle enhancement.
• Security of Home, "Peace of mind" focus.
Nice to have
• Pictures of "Press buttons for services available"
• Home control in one app. remote access from anywere.

```html
<!DOCTYPE html>
<html lang="en">
<head>
<meta charset="utf-8">
<title>Allwovenin – Home Automation Flyer</title>
<link href="https://fonts.googleapis.com/css2?family=Montserrat:wght@600;700;800&family=Oswald:wght@400;500;600&family=Roboto+Condensed:wght@400&family=Ubuntu:wght@400;500&display=swap" rel="stylesheet">
<style>
  :root{
    --stage:#2a2a2a;
    --screen-deep:#03101c;
    --screen-mid:#0c3a5e;
    --screen-glow:#1666a3;
    --bar-dark:#111;
    --bar-light:#3b3b3b;
    --red:#e01e26;
    --white:#ffffff;
    --ink:#1a1a1a;
    --paper:#f7f7f7;
    --rule:#6b6b6b;
    --label:#e6e6e6;
  }
  *{box-sizing:border-box;margin:0;padding:0}
  html,body{width:1200px;height:1029px;overflow:hidden}
  body{
    background:radial-gradient(ellipse at 50% 45%, #4a4a4a 0%, var(--stage) 70%);
    position:relative;
    font-family:"Ubuntu", sans-serif;
  }

  /* ---------- front face ---------- */
  .flyer-front{
    position:absolute;left:95px;top:95px;width:470px;height:840px;
    background:radial-gradient(ellipse at 50% 40%, var(--screen-glow) 0%, var(--screen-mid) 30%, var(--screen-deep) 75%);
    color:var(--white);overflow:hidden;
  }
  .room-bar{
    height:64px;background:linear-gradient(var(--bar-light),var(--bar-dark));
    display:flex;align-items:center;justify-content:flex-end;padding-right:10px;gap:10px;
    border-bottom:1px solid #000;
  }
  .room-name{font-size:18px;color:#ddd;padding:0 30px;border-left:1px solid #555;border-right:1px solid #555;margin-right:4px}
  .bar-button{width:54px;height:48px;border-radius:6px;background:linear-gradient(#5a5a5a,#1c1c1c);display:flex;align-items:center;justify-content:center;border:1px solid #000}
  .brand{text-align:center;margin-top:30px}
  .brand-name{display:inline-flex;align-items:center;gap:8px;font-family:"Montserrat",sans-serif;font-weight:800;font-size:36px;color:var(--white);letter-spacing:-.5px}
  .brand-square{width:14px;height:14px;background:var(--red)}
  .brand-tag{font-size:18px;color:#e8e8e8;margin-top:0}
  .control-grid{position:absolute;left:0;top:190px;width:100%;height:410px}
  .control{position:absolute;text-align:center;font-size:22px;color:var(--label);width:130px}
  .control .art{width:90px;height:80px;margin:0 auto 8px;border-radius:8px}
  .art-tv{background:linear-gradient(#9aa3ab,#2b3035)}
  .art-music{border-radius:50%!important;width:80px!important;background:radial-gradient(circle,#9fb0c0,#3a5a7a)}
  .art-lock{background:linear-gradient(#c8c8c8,#6f6f6f)}
  .art-bulb{border-radius:45% 45% 30% 30%!important;width:64px!important;background:radial-gradient(circle at 50% 35%,#f4f4f4,#8d8d8d)}
  .art-thermo{background:linear-gradient(#dcdcdc,#8a8a8a)}
  .art-gear{border-radius:50%!important;width:78px!important;background:radial-gradient(circle,#6d7a86 20%,#b8c2cb 60%,#6e7780)}
  .headline{position:absolute;top:640px;width:100%;text-align:center;font-family:"Montserrat",sans-serif}
  .headline .line-a{font-size:32px;font-weight:700;letter-spacing:.5px}
  .headline .line-b{font-size:25px;font-weight:700;color:var(--red);margin-top:-2px}
  .headline .line-c{font-size:15.5px;font-weight:700;line-height:1.2;margin-top:4px}
  .front-url{position:absolute;top:745px;width:100%;text-align:center;font-size:16px;letter-spacing:7px;color:#f0f0f0}
  .front-foot{position:absolute;bottom:0;width:100%;height:70px;background:linear-gradient(#4a4a4a 0,#1a1a1a 35%,#000 36%)}

  /* ---------- back face ---------- */
  .flyer-back{
    position:absolute;left:635px;top:95px;width:470px;height:840px;background:var(--paper);color:var(--ink);
    border-top:6px solid var(--rule);border-bottom:6px solid var(--rule);
  }
  .back-title{margin-top:58px;text-align:center;font-family:"Oswald",sans-serif;font-weight:600;line-height:1}
  .back-title .red{color:var(--red);font-size:48px;letter-spacing:.5px}
  .back-title .dark{font-size:40px;font-weight:500;margin-top:6px}
  .services-pill{margin:38px auto 0;width:250px;height:48px;border-radius:24px;background:var(--red);text-align:center;
    font-family:"Oswald",sans-serif;font-size:30px;font-weight:500;line-height:48px;color:var(--ink)}
  .services{display:grid;grid-template-columns:1fr 1fr;gap:0 34px;padding:20px 14px 0 22px;font-family:"Roboto Condensed",sans-serif;font-size:12.6px;line-height:1.4}
  .services ul{list-style:none}
  .services li{position:relative;padding-left:7px;margin-bottom:8px}
  .services li::before{content:"";position:absolute;left:0;top:6px;width:3px;height:3px;border-radius:50%;background:var(--red)}
  .features{padding:52px 22px 0 36px;font-family:"Roboto Condensed",sans-serif;font-size:12.6px;line-height:1.42}
  .features p{margin-bottom:16px}
  .back-url{text-align:center;font-size:15px;letter-spacing:7px;margin-top:22px}
</style>
</head>
<body>

<section class="flyer-front">
  <header class="room-bar">
    <span class="room-name">Family Room</span>
    <span class="bar-button">
      <svg width="22" height="28" viewBox="0 0 22 28"><circle cx="11" cy="10" r="8" fill="#eee"/><rect x="7" y="18" width="8" height="7" rx="1" fill="#aaa"/></svg>
    </span>
    <span class="bar-button">
      <svg width="32" height="24" viewBox="0 0 32 24"><path d="M2 8h6l7-6v20l-7-6H2z" fill="#eee"/><path d="M19 7q4 5 0 10M23 4q7 8 0 16" stroke="#eee" stroke-width="2" fill="none"/></svg>
    </span>
  </header>

  <div class="brand">
    <div class="brand-name"><span class="brand-square"></span>allwovenin</div>
    <div class="brand-tag">evolve your home</div>
  </div>

  <div class="control-grid">
    <div class="control" style="left:85px;top:0"><div class="art art-tv" role="img" aria-label="Flat screen television"></div>Watch</div>
    <div class="control" style="left:250px;top:0"><div class="art art-music" role="img" aria-label="Music speaker disc with note"></div>Listen</div>
    <div class="control" style="left:10px;top:115px"><div class="art art-lock" role="img" aria-label="Padlock with security camera"></div>Security</div>
    <div class="control" style="left:330px;top:115px"><div class="art art-bulb" role="img" aria-label="Light bulb"></div>Lighting</div>
    <div class="control" style="left:85px;top:230px"><div class="art art-thermo" role="img" aria-label="Thermostat showing 73 degrees"></div>Comfort</div>
    <div class="control" style="left:250px;top:230px"><div class="art art-gear" role="img" aria-label="Settings gear"></div>More...</div>
  </div>

  <div class="headline">
    <div class="line-a">VOICE CONTROL FOR</div>
    <div class="line-b">YOUR ENTIRE SMART HOME</div>
    <div class="line-c">HEARTHLY VOICE &amp; HOMEVIA9 DELIVER<br>HANDS-FREE HOME AUTOMATION</div>
  </div>
  <div class="front-url">www.homevia9.com</div>
  <div class="front-foot"></div>
</section>

<section class="flyer-back">
  <h1 class="back-title">
    <div class="red">EVOLVE YOUR HOME</div>
    <div class="dark">NOW AND BE CONNECTED</div>
  </h1>
  <div class="services-pill">OUR SERVICES</div>

  <div class="services">
    <ul>
      <li>Main/Sub Boards and Automation (smart home) controllers.</li>
      <li>Telephone, Data/Internet setup, TV, CCTV, Intercom/PABX</li>
      <li>Home theatre, multi room audio, sources central or local. Speakers.</li>
      <li>Multi room, music or video in any or all room flexibility. Coupled with high quality audio and HD video.</li>
      <li>Touch Panels (in wall or wireless), Monitors, OLED, LCD, LED Televisions</li>
    </ul>
    <ul>
      <li>Movement detectors for lighting, flood lighting.</li>
      <li>Stainless/Glass/Stone power and light switches.</li>
      <li>Alarm systems, detectors</li>
      <li>CCTV Camera styles. Indoor/Outdoor IP/analogue</li>
      <li>Windows, Awnings, Blinds control (wind rain sensors) Light fittings, LED lighting, specifications and design.</li>
    </ul>
  </div>

  <div class="features">
    <p>Décor-Friendly Gadgets. Home automation technology can blend in better with your décor</p>
    <p>Wireless Power Controls. Home automation allows you to control myriad devices with the touch of your finger.</p>
    <p>Automated Door Locks. If you're carrying heavy grocery bags or a crying child, unlocking your door can be quite a feat. Smart locks take the guesswork out of using a key by automating your front door to unlock or even open as you approach.</p>
    <p>Advanced Security Systems. Watch your kids get home safely from school, make sure they're doing their homework and not watching TV, or simply set up and arm your security system and other alarms while you're away with the touch of a button.</p>
  </div>
  <div class="back-url">www.homevia9.com</div>
</section>

</body>
</html>
```